Flyer Design for a Boston Therapeutic Clinic

I am a body therapist who needs a couple of flyers designed:
1. To fit half a page.
2. To fit a 5 inch by 3.5 inch flyer.
My practice is based in Boston, MA and my web site is:
www.LarkfieldTane.Com
For the First half page:
A. Have my company's name and color shown as it appears on my web site (Larkfield Tane)
B. Have the following text: "Control your weight (This part should be emphasized) by balancing your nervous and digestive system through the Tane Method. The Tane Method, a technique developed by Dr. Wenna. Tane, uses physical pressure to manipulate visceral tissue to bring back resiliency and proper functioning of the whole body."
Also helps with
-Constipation
-Bloating
-IBS
-eating disorders and overeating
Our practitioner is highly experienced. Please visit our web sites for reviews.
C. I would like to have a nice earthy feeling, something that feels "freeing" like open flowers, or an open land scape such as mountains or fields.
D. I also like the color blue, white, orange; perhaps if these colors can be integrated into the flyer, that would be great.
E. "Visit our web site LarkfieldTane.com or call 413-908-2617"
The Smaller Flyer :
A.The smaller Flyer should also have my Company's name as shown on my web site (Larkfield Tane)
B.The following text: " Restore your body's natural resiliency and greatly reduce your physical pain through the Dr. Wenna Tane Method of Structural Integration."
C. "Our practitioner is highly experienced and has a great reputation; visit our web site for reviews."
"Benefits:
"reduce aches and pains
reduce joint pain
reduce chronic muscular tension"
D, "feel better after the first session!"
E. if you could use a picture of me working on someone from my web site, that would be great.
F. I also like the colors white, orange and silver, for this one.
G. "Visit our web site LarkfieldTane.com or call 413-908 2617"
I am very open minded,
I would like the flyer to evoke a sense of tranquility, professionalism, and simplicity. So if you have another angle you think would look good, then go for it! As long as it looks clean, professional and helpful.
Thanks a lot!
If you need any pictures from my web site, I have the original high resolution files that i can send.
Professionals and working men and women from ages 20-70
Clinic

```html
<!DOCTYPE html>
<html lang="en">
<head>
<meta charset="utf-8">
<title>Larkfield Tane Therapy – Flyers</title>
<link rel="stylesheet" href="https://fonts.googleapis.com/css2?family=Alfa+Slab+One&family=Roboto+Slab:wght@300;400;600&display=swap">
<style>
  :root{
    --stage:#2b2b2b;
    --paper:#f7f5f2;
    --orange:#f0531c;
    --orange-soft:#f58a3a;
    --blue:#1e4fa8;
    --rust:#8a3510;
    --rust-dark:#4a1a08;
    --ink:#1c1c1c;
    --grey:#555a5e;
    --rule:#c9c9c9;
    --white:#ffffff;
  }
  *{margin:0;padding:0;box-sizing:border-box}
  html,body{width:1200px;height:750px;overflow:hidden;background:var(--stage)}
  .stage{position:relative;width:1200px;height:750px}
  .flyer{position:absolute;background:var(--paper);overflow:hidden;box-shadow:0 10px 30px rgba(0,0,0,.55)}
  .slab-heavy{font-family:"Alfa Slab One",serif;font-weight:400}
  .slab{font-family:"Roboto Slab",serif}

  /* ---------- half-page flyer ---------- */
  .flyer--weight{left:80px;top:40px;width:480px;height:670px}
  .weight__photo{position:absolute;left:270px;top:0;width:210px;height:670px;
    background:radial-gradient(ellipse at 45% 35%,#c96a35 0%,#a2461a 35%,var(--rust) 60%,var(--rust-dark) 100%)}
  .weight__stripe-blue{position:absolute;left:258px;top:88px;width:8px;height:582px;background:var(--blue)}
  .weight__stripe-orange{position:absolute;left:262px;top:270px;width:12px;height:400px;background:var(--orange)}
  .weight__title{position:absolute;left:48px;top:20px;font-size:38px;line-height:1;color:var(--orange);white-space:nowrap}
  .weight__subtitle{position:absolute;left:48px;top:68px;font-size:23px;line-height:1;color:var(--blue);white-space:nowrap}
  .weight__body{position:absolute;left:44px;top:108px;width:205px;font-size:15px;line-height:1.36;color:var(--ink)}
  .weight__body p+p{margin-top:18px}
  .weight__helps{position:absolute;left:24px;top:392px;width:226px;font-size:17px;line-height:1.2;color:var(--blue);
    border-bottom:1px solid var(--rule);padding-bottom:3px;white-space:nowrap}
  .weight__list{position:absolute;left:24px;top:422px;width:226px;list-style:none;font-size:12px;line-height:1.38;color:var(--ink)}
  .weight__list li{position:relative;padding-left:18px}
  .weight__list li::before{content:"";position:absolute;left:2px;top:5px;width:7px;height:7px;border-radius:50%;background:var(--orange)}
  .weight__note{position:absolute;left:14px;top:500px;width:238px;font-size:9.5px;font-weight:600;line-height:1.45;color:var(--orange);text-transform:uppercase}
  .weight__brand{position:absolute;left:12px;top:548px;width:240px;font-size:20px;font-weight:300;color:var(--grey);white-space:nowrap}
  .weight__brand .accent{color:var(--orange)}
  .weight__phone{position:absolute;left:8px;top:590px;width:246px;display:flex;align-items:center;gap:6px;font-size:34px;font-weight:300;color:var(--orange);white-space:nowrap}
  .weight__url{position:absolute;left:430px;top:335px;transform:translate(-50%,-50%) rotate(90deg);white-space:nowrap;
    font-size:17px;color:var(--white);letter-spacing:9px}

  /* ---------- small flyer ---------- */
  .flyer--relief{left:650px;top:90px;width:420px;height:580px;
    background:linear-gradient(100deg,var(--paper) 0%,var(--paper) 48%,#f8c9a0 68%,var(--orange-soft) 85%,var(--orange) 100%)}
  .relief__photo{position:absolute;left:190px;top:0;width:230px;height:340px;
    background:
      linear-gradient(to right,var(--paper) 0%,rgba(247,245,242,0) 40%),
      linear-gradient(to bottom,rgba(245,138,58,0) 65%,rgba(245,138,58,1) 100%),
      radial-gradient(ellipse at 60% 30%,#d8894a 0%,#c24a18 40%,#5a1d0a 80%,#2a0d05 100%)}
  .relief__figure{position:absolute;left:230px;top:325px;width:140px;height:200px;border-radius:40% 40% 30% 30%;
    background:radial-gradient(ellipse at center,rgba(210,210,210,.7) 0%,rgba(190,190,190,.3) 55%,transparent 75%)}
  .relief__brand{position:absolute;left:16px;top:30px;font-size:44px;line-height:1.1;font-weight:300;color:var(--orange);white-space:nowrap}
  .relief__brand-sub{position:absolute;left:20px;top:86px;font-size:25px;line-height:1.1;font-weight:300;color:var(--grey);white-space:nowrap}
  .relief__intro{position:absolute;left:20px;top:130px;width:230px;font-size:13px;line-height:1.35;color:var(--ink)}
  .relief__reputation{position:absolute;left:28px;top:252px;width:235px;font-size:12.5px;line-height:1.3;color:var(--grey);text-transform:uppercase;
    border-top:1px solid var(--rule);padding-top:6px}
  .relief__benefits-title{position:absolute;left:32px;top:362px;width:220px;font-size:17px;line-height:1.2;color:var(--orange);
    border-bottom:1px solid var(--rule);padding-bottom:3px}
  .relief__list{position:absolute;left:32px;top:392px;width:210px;list-style:none;font-size:13px;line-height:1.25;color:var(--ink)}
  .relief__list li{position:relative;padding-left:13px;margin-bottom:20px}
  .relief__list li::before{content:"";position:absolute;left:0;top:5px;width:8px;height:8px;border-radius:50%;background:var(--orange)}
  .relief__phone{position:absolute;left:36px;top:510px;display:flex;align-items:center;gap:6px;font-size:32px;font-weight:300;color:var(--orange);white-space:nowrap}
  .relief__tagline{position:absolute;left:362px;top:330px;transform:translate(-50%,-50%) rotate(-90deg);white-space:nowrap;
    font-size:15px;color:var(--white)}
  .relief__url{position:absolute;left:394px;top:400px;transform:translate(-50%,-50%) rotate(-90deg);white-space:nowrap;
    font-size:13px;color:var(--white);letter-spacing:6px}
</style>
</head>
<body>
<main class="stage">

  <section class="flyer flyer--weight">
    <div class="weight__photo" role="img" aria-label="Photo of a thoughtful man in warm rust tones"></div>
    <div class="weight__stripe-blue"></div>
    <div class="weight__stripe-orange"></div>

    <h1 class="weight__title slab-heavy">CONTROL</h1>
    <h2 class="weight__subtitle slab-heavy">YOUR WEIGHT</h2>
    <div class="weight__body slab">
      <p>by balancing your nervous and digestive system through theTane Method.</p>
      <p>The Tane Method, a technique developed by Dr. Wenna. Tane, uses physical pressure to manipulate visceral tissue to bring back resiliency and proper functioning of the whole body.</p>
    </div>
    <h3 class="weight__helps slab-heavy">ALSO HELPS WITH</h3>
    <ul class="weight__list slab">
      <li>Constipation</li>
      <li>Bloating</li>
      <li>IBS</li>
      <li>Psychological eating disorders</li>
    </ul>
    <p class="weight__note slab">Our practitioner is highly experienced.<br>Please visit our web sites for reviews</p>
    <p class="weight__brand slab"><span class="accent">Larkfield</span> Tane Therapy</p>
    <p class="weight__phone slab">
      <svg width="28" height="32" viewBox="0 0 24 24" aria-hidden="true"><path fill="#555a5e" d="M6.6 10.8c1.4 2.8 3.8 5.1 6.6 6.6l2.2-2.2c.3-.3.7-.4 1-.2 1.1.4 2.3.6 3.6.6.6 0 1 .4 1 1V20c0 .6-.4 1-1 1C10.6 21 3 13.4 3 4c0-.6.4-1 1-1h3.5c.6 0 1 .4 1 1 0 1.3.2 2.5.6 3.6.1.3 0 .7-.2 1z"/></svg>
      413-908-2617
    </p>
    <p class="weight__url slab">www.larkfieldtane.com</p>
  </section>

  <section class="flyer flyer--relief">
    <div class="relief__photo" role="img" aria-label="Photo of the practitioner working with a client"></div>
    <div class="relief__figure" role="img" aria-label="Illustration of an arm and shoulder skeleton"></div>

    <h1 class="relief__brand slab">Larkfield</h1>
    <h2 class="relief__brand-sub slab">Tane Therapy</h2>
    <p class="relief__intro slab">Restore your body's natural resiliency and greatly reduce your physical pain through the Dr. Wenna Tane Method of Structural Integration.</p>
    <p class="relief__reputation slab">Our practitioner is highly experienced and has a great reputation; visit our web site for reviews</p>
    <h3 class="relief__benefits-title slab-heavy">BENEFITS:</h3>
    <ul class="relief__list slab">
      <li>reduce aches and pain</li>
      <li>reduce joint pain</li>
      <li>reduce chronic muscular tension</li>
    </ul>
    <p class="relief__phone slab">
      <svg width="26" height="30" viewBox="0 0 24 24" aria-hidden="true"><path fill="#555a5e" d="M6.6 10.8c1.4 2.8 3.8 5.1 6.6 6.6l2.2-2.2c.3-.3.7-.4 1-.2 1.1.4 2.3.6 3.6.6.6 0 1 .4 1 1V20c0 .6-.4 1-1 1C10.6 21 3 13.4 3 4c0-.6.4-1 1-1h3.5c.6 0 1 .4 1 1 0 1.3.2 2.5.6 3.6.1.3 0 .7-.2 1z"/></svg>
      413-908-2617
    </p>
    <p class="relief__tagline slab-heavy">FEEL BETTER AFTER THE FIRST SESSION!</p>
    <p class="relief__url slab">www.LarkfieldTane.com</p>
  </section>

</main>
</body>
</html>
```